Concert Venue Show Posters (ongoing job too)

Looking for a designer for ongoing project to create posters for each of our concerts coming to the venue. We have a budget of $35-45.00 per poster and on average do 5-12 per month. We’re looking for simple, unique design template going forward as part of our branding.

We hope to establish a long term relationship with someone to do this work on an ongoing adhoc basis.

Goal is to simple tell folks who, where, and when.

Creative needs to delivered in Photoshop PSD file format in two sizes; 24" x 36" used onsite in lobby and 11" x 17" for offsite marketing distribution.

We’ll supply all approved artwork and information for you to use although sometimes what we get from management sucks.

You can look at some of our older posters here
http://bramblehallvenue.example-photos.com/Other/Posters/

Our website (it’s in re-design now)
http://www.bramblehallvenue.example

Our new website format moving toward this as template
http://www.copperlanternhall.example/event/252331-kestrel-owls-portland/

Thoughts? Ideas? Included artwork to see some samples.

Include these items on poster
Bramble HALL logo
Artists Name
Dorian Pike and the Lanterns (image with single guitar players)
Velvet Anchor (group image)
September 25, 2014
Doors 7:00
Show 8:00
You can sort of get an idea from our old posters.

PS this could lead to extra work doing our newspaper creatives too.
Updates

Project Deadline Extended
Reason: Due to weekend and workload of staff we'll make our final selection on Wednesday, August 28th by 6 PM EST. Thanks to everyone for submitting some great examples of work.

Target Market(s)

Onsite concert goers for future shows, and offsite spreading the word about shows.

Industry/Entity Type

Marketing

Requirements
Must have
• Simple is best. Not looking for bar band type posters, remember we're just letting fans know about who and when.
Nice to have
• Template, easy to reproduce show after show to keep costs down.
Should not have
• Less is more since we're just telling patons who, when, and where.

```html
<!DOCTYPE html>
<html lang="en">
<head>
<meta charset="utf-8">
<title>Dorian Pike and the Lanterns — Bramble HALL</title>
<link rel="stylesheet" href="https://fonts.googleapis.com/css2?family=Fredoka:wght@500;600&display=swap">
<style>
  :root {
    --page-bg: #eef0f0;
    --poster-dark: #17292e;
    --poster-band: #1f363b;
    --ink: #ffffff;
    --light-yellow: #f4f27a;
    --light-green: #8fd35a;
    --light-blue: #3f8fd6;
    --light-violet: #5b4fb8;
  }
  * { box-sizing: border-box; margin: 0; padding: 0; }
  html, body {
    width: 1200px;
    height: 900px;
    overflow: hidden;
    background: var(--page-bg);
  }
  .canvas {
    position: relative;
    width: 1200px;
    height: 900px;
    display: flex;
    align-items: center;
    justify-content: center;
  }
  .poster {
    position: relative;
    width: 560px;
    height: 840px;
    overflow: hidden;
    color: var(--ink);
    font-family: "Fredoka", "Arial Rounded MT Bold", sans-serif;
    text-align: center;
    background:
      repeating-linear-gradient(90deg,
        var(--poster-dark) 0 62px,
        var(--poster-band) 62px 124px);
  }
  .venue-name {
    position: absolute;
    top: 26px;
    left: 0;
    right: 0;
    font-weight: 600;
    font-size: 34px;
    line-height: 1;
    letter-spacing: 1px;
  }
  .headliner {
    position: absolute;
    top: 112px;
    left: 0;
    right: 0;
    font-weight: 600;
    line-height: 1.05;
  }
  .headliner .lead {
    display: block;
    font-size: 54px;
  }
  .headliner .band {
    display: block;
    font-size: 40px;
  }
  .stage-photo {
    position: absolute;
    top: 250px;
    left: 0;
    width: 100%;
    height: 390px;
    background:
      radial-gradient(ellipse 38% 30% at 28% 40%, rgba(244,242,122,0.95), transparent 70%),
      radial-gradient(ellipse 30% 26% at 82% 22%, rgba(244,242,122,0.85), transparent 70%),
      radial-gradient(ellipse 60% 45% at 50% 45%, rgba(143,211,90,0.75), transparent 75%),
      radial-gradient(ellipse 55% 40% at 55% 80%, rgba(63,143,214,0.8), transparent 75%),
      radial-gradient(ellipse 40% 30% at 20% 85%, rgba(91,79,184,0.7), transparent 75%);
    -webkit-mask-image: linear-gradient(180deg, transparent 0%, #000 18%, #000 78%, transparent 100%);
            mask-image: linear-gradient(180deg, transparent 0%, #000 18%, #000 78%, transparent 100%);
  }
  .show-date {
    position: absolute;
    top: 654px;
    left: 0;
    right: 0;
    font-weight: 600;
    font-size: 44px;
    line-height: 1;
  }
  .show-times {
    position: absolute;
    top: 710px;
    left: 0;
    right: 0;
    font-weight: 600;
    font-size: 24px;
    word-spacing: 6px;
  }
  .support-badge {
    position: absolute;
    top: 762px;
    left: 50%;
    width: 56px;
    height: 56px;
    margin-left: -28px;
  }
</style>
</head>
<body>
  <div class="canvas">
    <article class="poster">
      <div class="venue-name">Bramble HALL</div>

      <h1 class="headliner">
        <span class="lead">Dorian Pike</span>
        <span class="band">and the Lanterns</span>
      </h1>

      <div class="stage-photo" role="img" aria-label="Concert photo of a guitarist playing under yellow, green and blue stage lights"></div>

      <p class="show-date">September 25, 2014</p>
      <p class="show-times">Doors 7:00 &nbsp;Show 8:00</p>

      <svg class="support-badge" viewBox="0 0 56 56" role="img" aria-label="Velvet Anchor support act badge">
        <circle cx="28" cy="28" r="26" fill="none" stroke="#ffffff" stroke-width="2.5"/>
      </svg>
    </article>
  </div>
</body>
</html>
```